Course Lantern

CourseLantern.example will be a place for people looking for information, resources, and advisement to start or continue their education. We want a friendly, inviting site design that makes finding what potential students are looking for simple and easy to navigate. We are not committed to the colors of the logo, so variations on the color scheme are welcome.

Text instructions based on the wireframe: For the site's homepage we'd like a banner at the very top for our Logo and white space to the right of it. See attachments for logo + wireframe. Below that would be navigation. Below that split into 2/3 on the left we would have home page content, and 1/3 on the right we would have the lead form. At the bottom of the page we would have a space for types of degrees, then a footer with copyright info + site info.

See wireframes for additional page layouts.

Industry/Entity Type

Education

Requirements
Must have
• At minimum we are looking for three pages: homepage, choose your degree path page, and content page.
Nice to have
• -White space is appreciated
-Variations on the color scheme are welcome, we are not married to the existing logo's color scheme.

```html
<!DOCTYPE html>
<html lang="en">
<head>
<meta charset="utf-8">
<title>Course Lantern — Articles</title>
<link href="https://fonts.googleapis.com/css2?family=Ubuntu:wght@400;500;700&family=Arimo:wght@400;700&display=swap" rel="stylesheet">
<style>
:root{
  --navy:#1c4b67;
  --band:#235a78;
  --orange:#e8621a;
  --heading:#1f5a7a;
  --text:#4a4a4a;
  --light:#ececec;
  --footer:#3b3b3b;
}
*{box-sizing:border-box;margin:0;padding:0}
html,body{width:900px;height:1200px;overflow:hidden}
body{position:relative;background:#fff;font-family:"Ubuntu",sans-serif;color:var(--text)}
.abs{position:absolute}
.topbar{left:0;top:0;width:900px;height:44px;background:var(--navy)}
.contact-line{right:190px;top:14px;color:#fff;font-size:11.5px;font-weight:700}
.search{left:740px;top:9px;width:130px;height:22px;background:#fff;border:1px solid #c9c9c9;border-radius:2px;font-size:9px;color:#aaa;padding:5px 9px;font-family:"Arimo",sans-serif}
.search svg{position:absolute;right:6px;top:6px}
.header{left:0;top:44px;width:900px;height:93px;background:linear-gradient(#f3f3f3,#e6e6e6)}
.brand{left:31px;top:84px;display:flex;align-items:center;gap:10px}
.brand-mark{width:18px;height:18px;background:var(--orange)}
.brand-name{font-size:36px;font-weight:500;color:var(--navy);letter-spacing:-.5px}
.address{right:32px;top:68px;text-align:right;font-size:11px;line-height:15.5px;color:#333}
.nav{left:0;top:137px;width:900px;height:45px;background:linear-gradient(#fafafa,#e9e9e9);border-top:1px solid #ddd}
.nav ul{list-style:none;display:flex;position:absolute;left:97px;top:12px;font-size:12px;color:#333}
.nav li{padding:5px 0;margin-right:32px}
.nav li.active{background:var(--band);color:#fff;padding:5px 10px;border-radius:2px;margin-right:22px}
.hero{left:0;top:182px;width:900px;height:274px;background:var(--band)}
.crumbs{right:100px;top:11px;font-size:10px;color:#fff}
.crumbs b{color:var(--orange);font-weight:400}
.slide-frame{left:91px;top:33px;width:718px;height:191px;background:#f1f1f1;border-radius:3px;padding:10px}
.slide{width:698px;height:172px;display:flex;background:linear-gradient(90deg,#cfcfd1 0%,#e9e9e9 45%,#fafafa 65%,#f6f6f6 100%)}
.slide-photo{width:360px;height:100%;background:linear-gradient(135deg,#b9b2ab,#8d8680 50%,#d2cfcb)}
.slide-title{flex:1;display:flex;align-items:center;justify-content:center;font-size:21px;color:var(--orange);padding-left:20px}
.arrow{top:128px}
.section-mark{left:48px;top:494px;width:20px;height:20px;background:var(--orange)}
.section-title{left:80px;top:497px;font-size:20px;font-weight:400;color:var(--orange)}
.section-title span{color:var(--heading)}
.dots{left:48px;top:532px;width:485px;border-top:2px dotted #aaa}
.article-title{left:48px;top:548px;font-size:17px;font-weight:400;color:var(--heading)}
.para{font-size:10.3px;line-height:15.4px;text-align:justify;color:#4a4a4a;letter-spacing:-.1px}
.p1{left:48px;top:584px;width:241px}
.article-body{left:48px;top:718px;width:477px}
.article-body p+p{margin-top:15px}
.article-photo{left:304px;top:586px;width:221px;height:117px;border:1px solid #ddd;background:linear-gradient(90deg,#e8d7c6,#bfa89a 40%,#e1c0b9 75%,#f1e6e2)}
.view-more{right:375px;top:975px;font-size:11px;color:var(--heading)}
.degrees{left:43px;top:1013px;width:490px;height:91px;background:#e3e3e3;border-radius:2px}
.degrees-inner{position:absolute;left:14px;top:0;right:14px;height:91px;background:#ececec}
.degrees h3{position:absolute;left:6px;top:13px;font-size:11.5px;font-weight:400;color:var(--heading)}
.degree-item{position:absolute;top:38px;width:200px;font-size:10.5px;color:#333}
.degree-item p{margin-top:8px;font-size:9.3px;line-height:13.5px;color:#666;padding-left:10px}
.chev{position:absolute;top:43px;font-size:10px;color:#777}
.tell{left:578px;top:468px;font-family:"Arimo",sans-serif;font-size:15.5px;font-weight:700;color:var(--heading)}
.tell-note{left:578px;top:495px;width:280px;font-family:"Arimo",sans-serif;font-size:9.8px;line-height:13.5px;color:#555}
.lead-form{left:567px;top:534px;width:291px;height:416px;background:#fff;border:1px solid #d6d6d6;font-family:"Arimo",sans-serif;box-shadow:0 1px 3px rgba(0,0,0,.08)}
.form-head{height:34px;background:var(--light);font-size:11.5px;color:#333;text-align:center;line-height:34px}
.row{position:absolute;left:11px;height:26px;display:flex;align-items:center;font-size:10.3px;color:#333}
.row i{color:var(--orange);font-style:normal}
.field{position:absolute;left:116px;width:166px;height:26px;background:linear-gradient(#ededed,#e1e1e1);border:1px solid #d2d2d2;border-radius:2px;font-size:10px;color:#666;padding:7px 10px}
.field.select::after{content:"";position:absolute;right:9px;top:10px;border:5px solid transparent;border-top:6px solid #555}
.btn{position:absolute;left:43px;top:374px;width:207px;height:30px;background:linear-gradient(#f7a039,#e8621a);border:1px solid #c85511;border-radius:3px;display:flex;align-items:center;justify-content:center;gap:18px;font-size:13px;font-weight:700;color:#222}
.form-foot{left:556px;top:962px;font-family:"Arimo",sans-serif;font-size:9.3px;color:#555}
.ad{left:628px;top:980px;width:153px;height:124px;border:1px solid #888;background:#fff;font-family:"Arimo",sans-serif;padding:7px 7px}
.ad h4{font-size:11.5px;color:#666;text-decoration:underline}
.ad p{font-size:10.8px;line-height:14.5px;color:#111;margin-top:2px}
.ad small{display:block;font-size:8.5px;color:#333;margin-top:2px}
.ad-bar{position:absolute;left:0;bottom:0;width:151px;height:14px;display:flex;align-items:center;gap:3px;padding-left:3px}
.ad-bar span{width:12px;height:11px;background:#999}
.ad-bar span+span{background:#333}
.ad-tag{margin-left:auto;background:#888;color:#fff;font-size:8px;padding:2px 4px}
.footer{left:0;top:1114px;width:900px;height:86px;background:var(--footer);border-top:3px solid #ccc}
.foot-links{left:31px;top:20px;font-size:10px;color:#ddd}
.foot-links span{margin:0 6px;color:#999}
.copy{left:31px;top:45px;font-size:10px;color:#ddd}
.social{left:730px;top:30px;display:flex;gap:7px}
.social span{width:22px;height:22px;border-radius:50%;background:#fff}
</style>
</head>
<body>
<div class="abs topbar">
  <div class="abs contact-line">Telephone: 555-014-2200 &nbsp;|&nbsp; Facsimile: 555-014-2201</div>
  <div class="abs search">Search
    <svg width="9" height="9" viewBox="0 0 10 10"><circle cx="4" cy="4" r="3" fill="none" stroke="#aaa" stroke-width="1.2"/><line x1="6.2" y1="6.2" x2="9" y2="9" stroke="#aaa" stroke-width="1.4"/></svg>
  </div>
</div>

<header class="abs header"></header>
<div class="abs brand"><div class="brand-mark"></div><div class="brand-name">Course Lantern</div></div>
<div class="abs address">CourseLantern.example<br>48 Orchard Hill Lane<br>Fairbrook, OR 97000</div>

<nav class="abs nav">
  <ul>
    <li class="active">Home</li><li>About Us</li><li>Degrees</li><li>How it works</li><li>Contact Us</li><li>Feedback</li><li>Terms and Conditions</li><li>Privacy Policy</li>
  </ul>
</nav>

<section class="abs hero">
  <div class="abs crumbs"><b>Home</b> &nbsp;&gt;&nbsp; Articles</div>
  <div class="abs slide-frame">
    <div class="slide">
      <div class="slide-photo" role="img" aria-label="Group of students studying together around a table"></div>
      <div class="slide-title">Invest In Your Future Today!</div>
    </div>
  </div>
  <svg class="abs arrow" style="left:45px" width="28" height="36" viewBox="0 0 28 36"><polyline points="22,3 7,18 22,33" fill="none" stroke="#e8e8e8" stroke-width="6"/></svg>
  <svg class="abs arrow" style="left:825px" width="28" height="36" viewBox="0 0 28 36"><polyline points="6,3 21,18 6,33" fill="none" stroke="#e8e8e8" stroke-width="6"/></svg>
</section>

<div class="abs section-mark"></div>
<h2 class="abs section-title">Our <span>Articles</span></h2>
<div class="abs dots"></div>
<h1 class="abs article-title">Excepteur sint occaecat cupidatat non proident, sunt in culpa</h1>

<p class="abs para p1">Sed ut perspiciatis unde omnis iste natus error sit voluptatem accusantium doloremque laudantium, totam rem aperiam, eaque ipsa quae ab illo inven tore veritatis et quasi architecto beatae vitae dicta sunt explicabo. Nemo enim ipsam voluptatem quia voluptas sit aspernatur aut odit aut fugit, sed quia consequuntur magni dolores eos qui ratione voluptatem sequi nesciunt.</p>
<div class="abs article-photo" role="img" aria-label="Smiling students holding books and folders"></div>
<div class="abs article-body">
<p class="para">But I must explain to you how all this mistaken idea of denouncing pleasure and praising pain was born and I will give you a complete account of the system, and expound the actual teachings of the great explorer of the truth, the master-builder of human happiness. No one rejects, dislikes, or avoids pleasure itself, because it is pleasure, but because those who do not know how to pursue pleasure rationally encounter consequences that are extremely painful. Nor again is there anyone who loves or pursues or desires to obtain pain of itself, because it is pain, but because occasionally circumstances occur in which toil and pain can procure him some great pleasure. To take a trivial example, which of us ever undertakes laborious physical exercise, except to obtain some advantage from it.</p>
<p class="para">At vero eos et accusamus et iusto odio dignissimos ducimus qui blanditiis praesentium voluptatum deleniti atque corrupti quos dolores et quas molestias excepturi sint occaecati cupiditate non provident, similique sunt in culpa qui officia deserunt mollitia animi, id est laborum et dolorum fuga. Et harum quidem rerum facilis est et expedita distinctio. Nam libero tempore, cum soluta nobis est eligendi optio cumque nihil impedit quo minus id quod maxime placeat facere possimus, omnis voluptas assumenda est, omnis dolor repellendus. Temporibus autem quibusdam et aut officiis debitis aut rerum necessitatibus saepe eveniet ut et voluptates repudiandae.</p>
</div>
<div class="abs view-more">View more</div>

<section class="abs degrees">
  <span class="chev" style="left:4px">&#8249;</span>
  <div class="degrees-inner">
    <h3>Which type of degree you want</h3>
    <div class="degree-item" style="left:24px">&#9656;&nbsp; Quis autem vel eum<p>reprehenderit qui in ea voluptate velit esse quam nihil velillum quidolorem.</p></div>
    <div class="degree-item" style="left:248px">&#9656;&nbsp; Quis autem vel eum<p>reprehenderit qui in ea voluptate velit esse quam nihil velillum quidolorem.</p></div>
  </div>
  <span class="chev" style="right:4px">&#8250;</span>
</section>

<h2 class="abs tell">Tell us more about YOU!</h2>
<p class="abs tell-note">Your information will be kept strictly private as stated in our Privacy Policy.</p>

<form class="abs lead-form">
  <div class="form-head">Get matched to the right schools today.</div>
  <div class="row" style="top:46px">Subject&nbsp;<i>*</i></div>
  <div class="field select" style="top:46px">Choose one</div>
  <div class="row" style="top:81px">Degree Level&nbsp;<i>*</i></div>
  <div class="field select" style="top:81px">Choose one</div>
  <div class="row" style="top:116px">High School Grad Yr&nbsp;<i>*</i></div>
  <div class="field select" style="top:116px">Choose one</div>
  <div class="row" style="top:151px">First Name&nbsp;<i>*</i></div>
  <div class="field" style="top:151px"></div>
  <div class="row" style="top:186px">Last Name&nbsp;<i>*</i></div>
  <div class="field" style="top:186px"></div>
  <div class="row" style="top:221px">Street Address&nbsp;<i>*</i></div>
  <div class="field" style="top:221px"></div>
  <div class="row" style="top:256px">Zip / City / State&nbsp;<i>*</i></div>
  <div class="field" style="top:256px;width:46px"></div>
  <div class="field" style="top:256px;left:168px;width:64px">City</div>
  <div class="field" style="top:256px;left:237px;width:45px">State</div>
  <div class="row" style="top:291px">Phone Number&nbsp;<i>*</i></div>
  <div class="field" style="top:291px"></div>
  <div class="row" style="top:326px">Email Address&nbsp;<i>*</i></div>
  <div class="field" style="top:326px"></div>
  <div class="btn">
    <svg width="12" height="15" viewBox="0 0 12 15"><path d="M3 7V4.5a3 3 0 0 1 6 0V7" fill="none" stroke="#222" stroke-width="1.8"/><rect x="0.5" y="7" width="11" height="8" rx="1" fill="#222"/></svg>
    Request Information
  </div>
</form>
<p class="abs form-foot">Your information will be kept strictly private as stated in our Privacy Policy.</p>

<aside class="abs ad">
  <h4>Affordable Hotels</h4>
  <p>Special rates until the end of the month. No booking fees, book your room now!</p>
  <small>www.example.com</small>
  <div class="ad-bar"><span></span><span></span><div class="ad-tag">Ads by Adnetic</div></div>
</aside>

<footer class="abs footer">
  <div class="abs foot-links">Home<span>|</span>About Us<span>|</span>Degrees<span>|</span>How it works<span>|</span>Contact Us<span>|</span>Feedback<span>|</span>Terms and Conditions<span>|</span>Privacy Policy<span>|</span>Sitemap</div>
  <div class="abs copy">Copyright © 2012 www.courselantern.example &nbsp;All rights reserved</div>
  <div class="abs social"><span></span><span></span><span></span><span></span><span></span></div>
</footer>
</body>
</html>
```